The Christian Teacher Life-Cycle

Look at the Lifecyle of the Christian School.
Look at the BLT logo.
I am looking for a Faithful Educator PATHWAY that represents the slides in the PP upload.
Our website is bramblewoodlearningtrust.org.
The design should include a summary design showing all four stages, and then four slides representing each of the stages as subsets of the summary design.
When a teacher is going through the Lifecycle, they are going on their Professional Learning Journey that takes 40 years to unfold.
All five should include a copyright 2026 BLT on them.

```html
<!DOCTYPE html>
<html lang="en">
<head>
<meta charset="utf-8">
<title>Faithful Educator Pathway – Slide Set</title>
<link rel="stylesheet" href="https://fonts.googleapis.com/css2?family=Playfair+Display:wght@400;600&family=Open+Sans:wght@400;600;700&display=swap">
<style>
:root{
  --board:#d8d8da;
  --paper:#ffffff;
  --brand-blue:#3b6fa8;
  --brand-blue-dark:#2f5f94;
  --title-grey:#5a5a5a;
  --text-grey:#555b61;
  --soft-blue:#e8f0f9;
  --hill:#8fae72;
  --hill-deep:#6f9458;
  --mist:#eef2f4;
}
*{box-sizing:border-box;margin:0;padding:0}
html,body{width:1200px;height:489px;overflow:hidden;background:var(--board)}
body{position:relative;font-family:"Open Sans",sans-serif;color:var(--text-grey)}
.slide{position:absolute;width:272px;height:205px;background:var(--paper);overflow:hidden}
.art{position:absolute}
.art-full{inset:0;background:linear-gradient(180deg,#dce8f3 0%,#c9dbe9 38%,#9fb9a0 60%,var(--hill) 78%,var(--hill-deep) 100%)}
.art-panel{background:linear-gradient(180deg,#e4ecf2 0%,#c7d8e6 35%,#9db99a 62%,var(--hill) 80%,var(--hill-deep) 100%)}
.art-fade{position:absolute;pointer-events:none}
.brand{position:absolute;left:9px;top:10px;display:flex;align-items:center;gap:3px}
.brand-mark{font-family:"Open Sans",sans-serif;font-weight:600;font-size:13px;color:var(--brand-blue);letter-spacing:.5px}
.heading{position:absolute}
.title{font-family:"Playfair Display",serif;font-weight:400;font-size:10px;line-height:1.2;color:var(--title-grey);white-space:nowrap;padding-bottom:1.5px;border-bottom:1px dotted var(--brand-blue)}
.title b{font-weight:400;color:var(--brand-blue)}
.subtitle{font-size:4.6px;line-height:1.2;color:var(--brand-blue);letter-spacing:.1px;margin-top:2px;white-space:nowrap}
.stage-title{position:absolute;font-family:"Playfair Display",serif;font-weight:400;font-size:10.5px;line-height:1.2;color:var(--brand-blue)}
.points{position:absolute;list-style:none;font-size:5px;line-height:5.8px;color:var(--text-grey)}
.points li{position:relative;padding-left:4px;margin-bottom:3.2px}
.points li::before{content:"•";position:absolute;left:0;color:var(--brand-blue)}
.points li.lead{font-weight:700;color:#3f4348}
.wave{position:absolute;left:0;bottom:0;width:272px;height:45px}
.motto{position:absolute;right:6px;bottom:6px;text-align:right;font-family:"Playfair Display",serif;font-size:5px;line-height:6.3px;color:#fff}
.motto b{font-weight:600}
.copyright{position:absolute;left:8px;bottom:4px;font-size:3.6px;color:#fff}
.slide.summary .motto{color:#4b4f55}
.slide.summary .motto b{color:var(--brand-blue)}
.slide.summary .copyright{color:#5a5f66}
.marker{position:absolute;font-size:4px;line-height:4.6px;color:#4b5560}
.marker strong{display:block;font-weight:600;color:var(--brand-blue-dark);font-size:4.4px}
.marker-line{position:absolute;width:0;border-left:.6px solid #58636e}
.growth-list{position:absolute;left:25px;top:66px;font-size:4.2px;line-height:5.2px;color:var(--text-grey)}
.growth-list div{display:flex;margin-bottom:4px}
.growth-list dt{width:26px;flex:none;font-family:"Playfair Display",serif;color:var(--brand-blue)}
.callout{position:absolute;left:12px;top:129px;width:181px;height:45px;background:var(--soft-blue);padding:5px 14px}
.callout h3{font-family:"Playfair Display",serif;font-weight:400;font-size:7.8px;line-height:1.2;color:var(--brand-blue);margin-bottom:4px}
.callout p{font-size:4px;line-height:4.8px;color:var(--text-grey)}
.stack-title{font-family:"Playfair Display",serif;font-weight:400;font-size:12px;line-height:14px;color:var(--title-grey);white-space:nowrap}
.stack-title.accent{display:inline-block;color:var(--brand-blue);border-bottom:1px dotted var(--brand-blue)}
</style>
</head>
<body>

<!-- Summary -->
<section class="slide summary" style="left:178px;top:32px">
  <div class="art art-full" role="img" aria-label="Illustrated hillside path rising from a teacher watering a seedling, past growing trees and groups of teachers, to a hilltop cross with children"></div>
  <div class="art-fade" style="left:0;top:0;width:272px;height:60px;background:linear-gradient(180deg,#fff 0%,rgba(255,255,255,.85) 55%,rgba(255,255,255,0) 100%)"></div>
  <header class="brand"><span class="brand-mark">BLT</span></header>
  <div class="heading" style="left:50px;top:13px">
    <h2 class="title">Faithful Educator <b>PATHWAY</b></h2>
    <p class="subtitle">A 40 YEAR PROFESSIONAL LEARNING JOURNEY</p>
  </div>
  <div class="marker" style="left:21px;top:101px;width:40px"><strong>Stage 1</strong>The focus is on “I”</div>
  <div class="marker-line" style="left:17px;top:103px;height:72px"></div>
  <div class="marker" style="left:73px;top:100px;width:44px"><strong>Stage 2</strong>Becoming part of the Christian Professional Learning Community</div>
  <div class="marker-line" style="left:70px;top:102px;height:30px"></div>
  <div class="marker" style="left:134px;top:59px;width:44px"><strong>Stage 3</strong>Learning leadership within the faculty culture/CPLC</div>
  <div class="marker-line" style="left:131px;top:61px;height:35px"></div>
  <div class="marker" style="left:196px;top:32px;width:62px"><strong>Stage 4</strong>So good, I am “invisible”; I have let go of control and share it with my children/teens</div>
  <div class="marker-line" style="left:193px;top:34px;height:26px"></div>
  <svg class="wave" viewBox="0 0 272 45" preserveAspectRatio="none" aria-hidden="true"><path d="M0 27 Q150 36 272 8 V45 H0Z" fill="#fff"/></svg>
  <p class="motto">In Faith<br>Through <b>Service</b><br>With Learners</p>
  <p class="copyright">© 2026 Bramblewood Learning Trust</p>
</section>

<!-- Stages of growth -->
<section class="slide" style="left:467px;top:32px">
  <div class="art art-panel" style="left:206px;top:0;width:66px;height:190px" role="img" aria-label="Young tree on a hillside path with misty blue mountains"></div>
  <header class="brand"><span class="brand-mark">BLT</span></header>
  <div class="heading" style="left:52px;top:14px">
    <h2 class="stack-title">Faithful Educator</h2>
    <h2 class="stack-title accent">PATHWAY</h2>
    <p class="subtitle" style="font-size:5.8px;margin-top:3px">STAGES OF GROWTH</p>
  </div>
  <dl class="growth-list">
    <div><dt>STAGE 1</dt><dd>The focus is on “I”</dd></div>
    <div><dt>STAGE 2</dt><dd>Becoming part of the Christian Professional<br>Learning Community</dd></div>
    <div><dt>STAGE 3</dt><dd>Learning leadership within the faculty culture/CPLC</dd></div>
    <div><dt>STAGE 4</dt><dd>So good, I am “invisible”; I have let go of control<br>and share it with my children/teens</dd></div>
  </dl>
  <div class="callout">
    <h3>All are good. The only sin is not growing.</h3>
    <p>It is a 40 year career-long Professional Learning Journey.<br>I want to grow so that children and teenagers<br>will become more than before.<br>They are also on a life-long Personal Learning Journey.</p>
  </div>
  <svg class="wave" viewBox="0 0 272 45" preserveAspectRatio="none" aria-hidden="true"><path d="M0 32 Q150 36 272 10 V45 H0Z" fill="var(--brand-blue)"/></svg>
  <p class="motto">In Faith<br>Through <b>Service</b><br>With Learners</p>
  <p class="copyright">© 2026 Bramblewood Learning Trust</p>
</section>

<!-- Stage 1 -->
<section class="slide" style="left:755px;top:32px">
  <div class="art art-panel" style="left:0;top:0;width:68px;height:190px" role="img" aria-label="Teacher watering a seedling beside a hillside path"></div>
  <div class="art-fade" style="left:0;top:0;width:68px;height:90px;background:linear-gradient(180deg,#fff 0%,rgba(255,255,255,0) 100%)"></div>
  <div class="art-fade" style="left:68px;top:60px;width:204px;height:140px;background:linear-gradient(90deg,var(--mist),#fff 60%)"></div>
  <header class="brand"><span class="brand-mark">BLT</span></header>
  <div class="heading" style="left:77px;top:14px">
    <h2 class="title" style="font-size:11.5px">Faithful Educator <b>PATHWAY</b></h2>
    <p class="subtitle">A 40 YEAR PROFESSIONAL LEARNING JOURNEY</p>
  </div>
  <h3 class="stage-title" style="left:82px;top:61px">Stage 1</h3>
  <ul class="points" style="left:79px;top:86px;width:190px">
    <li class="lead">The focus is on “I”</li>
    <li>Fundamental skills dominate such as classroom management</li>
    <li>Curriculum is where I spend my time</li>
    <li>I am a sponge rather than a contributor</li>
    <li>I see myself as a learner</li>
    <li>I reflect on my practice</li>
  </ul>
  <svg class="wave" viewBox="0 0 272 45" preserveAspectRatio="none" aria-hidden="true"><path d="M0 32 Q150 36 272 8 V45 H0Z" fill="var(--brand-blue)"/></svg>
  <p class="motto">In Faith<br>Through <b>Service</b><br>With Learners</p>
  <p class="copyright">© 2026 Bramblewood Learning Trust</p>
</section>

<!-- Stage 2 -->
<section class="slide" style="left:36px;top:250px">
  <div class="art art-panel" style="left:68px;top:50px;width:68px;height:150px" role="img" aria-label="Two teachers walking together on a path past a young tree"></div>
  <div class="art-fade" style="left:68px;top:50px;width:68px;height:50px;background:linear-gradient(180deg,#fff,rgba(255,255,255,0))"></div>
  <header class="brand"><span class="brand-mark">BLT</span></header>
  <div class="heading" style="left:77px;top:16px">
    <h2 class="title" style="font-size:11.5px">Faithful Educator <b>PATHWAY</b></h2>
    <p class="subtitle">A 40 YEAR PROFESSIONAL LEARNING JOURNEY</p>
  </div>
  <h3 class="stage-title" style="left:150px;top:57px">Stage 2</h3>
  <ul class="points" style="left:146px;top:81px;width:120px">
    <li class="lead">My Christian Professional Learning Community is important to me as a place where I give and take</li>
    <li>I recognize that “we” is more powerful for the child than “I”</li>
    <li>I know my curriculum - I am more focused on how, on pedagogy</li>
    <li>I assess relevant &amp; effective assessment tools</li>
    <li>I reflect on my practice</li>
  </ul>
  <svg class="wave" viewBox="0 0 272 45" preserveAspectRatio="none" aria-hidden="true"><path d="M0 32 Q150 36 272 8 V45 H0Z" fill="var(--brand-blue)"/></svg>
  <p class="motto">In Faith<br>Through <b>Service</b><br>With Learners</p>
  <p class="copyright">© 2026 Bramblewood Learning Trust</p>
</section>

<!-- Stage 3A -->
<section class="slide" style="left:324px;top:250px">
  <div class="art art-panel" style="left:136px;top:50px;width:68px;height:150px" role="img" aria-label="Teachers talking beside a leafy tree on a hillside path"></div>
  <div class="art-fade" style="left:136px;top:50px;width:68px;height:50px;background:linear-gradient(180deg,#fff,rgba(255,255,255,0))"></div>
  <header class="brand"><span class="brand-mark">BLT</span></header>
  <div class="heading" style="left:77px;top:14px">
    <h2 class="title" style="font-size:11.5px">Faithful Educator <b>PATHWAY</b></h2>
    <p class="subtitle">A 40 YEAR PROFESSIONAL LEARNING JOURNEY</p>
  </div>
  <h3 class="stage-title" style="left:21px;top:56px">Stage 3A</h3>
  <ul class="points" style="left:18px;top:80px;width:116px">
    <li class="lead">I lead in my Christian Professional Learning Community</li>
    <li>Ensuring my colleagues continue to grow is critical to me</li>
    <li>Together, we are humble in understanding where we still need to go</li>
    <li>My colleagues see me as an important resource</li>
    <li>I am a master of growth</li>
    <li>I help my colleagues reflect</li>
  </ul>
  <svg class="wave" viewBox="0 0 272 45" preserveAspectRatio="none" aria-hidden="true"><path d="M0 32 Q150 36 272 8 V45 H0Z" fill="var(--brand-blue)"/></svg>
  <p class="motto">In Faith<br>Through <b>Service</b><br>With Learners</p>
  <p class="copyright">© 2026 Bramblewood Learning Trust</p>
</section>

<!-- Stage 3B -->
<section class="slide" style="left:610px;top:250px;width:277px;height:207px">
  <div class="art art-panel" style="left:139px;top:50px;width:68px;height:157px" role="img" aria-label="Teacher kneeling beside a child reading on a hillside path under a tree"></div>
  <div class="art-fade" style="left:139px;top:50px;width:68px;height:50px;background:linear-gradient(180deg,#fff,rgba(255,255,255,0))"></div>
  <header class="brand"><span class="brand-mark">BLT</span></header>
  <div class="heading" style="left:78px;top:14px">
    <h2 class="title" style="font-size:11.5px">Faithful Educator <b>PATHWAY</b></h2>
    <p class="subtitle">A 40 YEAR PROFESSIONAL LEARNING JOURNEY</p>
  </div>
  <h3 class="stage-title" style="left:17px;top:57px">Stage 3B</h3>
  <ul class="points" style="left:14px;top:81px;width:122px">
    <li class="lead">I move to position the child as the owner of their own learning</li>
    <li>I give up control so the child can gain control</li>
    <li>The child becomes an architect in their curriculum</li>
    <li>The child becomes a collaborator in the how</li>
    <li>I am more a learner than a teacher</li>
    <li>I am a master of pedagogies</li>
    <li>I reflect on my practice through the eyes of children</li>
  </ul>
  <svg class="wave" viewBox="0 0 272 45" preserveAspectRatio="none" aria-hidden="true" style="width:277px"><path d="M0 32 Q150 36 272 8 V45 H0Z" fill="var(--brand-blue)"/></svg>
  <p class="motto">In Faith<br>Through <b>Service</b><br>With Learners</p>
  <p class="copyright">© 2026 Bramblewood Learning Trust</p>
</section>

<!-- Stage 4 -->
<section class="slide" style="left:902px;top:251px;width:280px;height:209px">
  <div class="art art-panel" style="left:210px;top:50px;width:70px;height:159px" role="img" aria-label="Teacher with children on a hilltop path near a cross and a large tree"></div>
  <div class="art-fade" style="left:210px;top:50px;width:70px;height:40px;background:linear-gradient(180deg,#fff,rgba(255,255,255,0))"></div>
  <header class="brand"><span class="brand-mark">BLT</span></header>
  <div class="heading" style="left:79px;top:15px">
    <h2 class="title" style="font-size:11.5px">Faithful Educator <b>PATHWAY</b></h2>
    <p class="subtitle">A 40 YEAR PROFESSIONAL LEARNING JOURNEY</p>
  </div>
  <h3 class="stage-title" style="left:16px;top:58px">Stage 4</h3>
  <ul class="points" style="left:14px;top:83px;width:192px">
    <li class="lead">I am comfortable both in making the child owner and in taking on leadership roles with colleagues</li>
    <li>Children come to and stay at the school because I am there</li>
    <li>I want and work to ensure that every child to succeed</li>
    <li>I want and work to ensure that every one of my colleagues to succeed</li>
    <li>I am a master of several pedagogies</li>
    <li>I am a master of metacognition</li>
    <li>I see myself as a learner</li>
    <li>I reflect on my practice with my children / teens</li>
  </ul>
  <svg class="wave" viewBox="0 0 272 45" preserveAspectRatio="none" aria-hidden="true" style="width:280px"><path d="M0 32 Q150 36 272 8 V45 H0Z" fill="var(--brand-blue)"/></svg>
  <p class="motto">In Faith<br>Through <b>Service</b><br>With Learners</p>
  <p class="copyright">© 2026 Bramblewood Learning Trust</p>
</section>

</body>
</html>
```